Letterhead for small civil engineer company

We need bold and modern design for company letterhead in MS word. It needs to have company logo and company info. Somewhere in the upper right part of document needs to be space for "recever" and the documents starts with, example, "SUBJECT: CIVIL ENGINEER LETTERHEAD".

in the bottom part of document needs to be signature and date.

Company info: Veltrana d.o.o., Lipovac 15, Lipovac (Općina Brdarić), OIB 47396028154, www.veltrana.hr, info@veltrana.hr

Email of document sender needs to be somewhere if document, exapmle xyz@veltrana.hr

Target Market(s)

Civil engineer company and projects

Industry/Entity Type

Civil engineer

Font styles to use
Serif

Colors
F0912C
F2A743
F7CA91
FBE8D2
FDF5EE

Requirements
Must have
• Company logo and company info
Nice to have
• Moder and clean design
Should not have
• Too much details

```html
<!DOCTYPE html>
<html lang="en">
<head>
<meta charset="utf-8">
<title>Veltrana Letterhead</title>
<link href="https://fonts.googleapis.com/css2?family=Source+Serif+4:wght@400;700&display=swap" rel="stylesheet">
<style>
  :root {
    --backdrop: #dcdcdc;
    --paper: #e9e8e8;
    --ink: #3f3f3f;
    --brand: #d97f2e;
    --brand-dark: #c8742e;
    --brand-frame: #555555;
    --footer-text: #fdf5ee;
    --signature-tone: #d6d4d4;
  }
  * { box-sizing: border-box; margin: 0; padding: 0; }
  html, body {
    width: 950px; height: 1200px; overflow: hidden;
    background: var(--backdrop);
    font-family: "Source Serif 4", Georgia, serif;
    color: var(--ink);
  }
  .letterhead {
    position: absolute; left: 46px; top: 0;
    width: 858px; height: 1200px;
    background: var(--paper);
  }
  .brand {
    position: absolute; left: 0; right: 0; top: 50px;
    display: flex; flex-direction: column; align-items: center; gap: 12px;
  }
  .brand-square {
    width: 69px; height: 69px;
    border: 2px solid var(--brand-frame);
  }
  .brand-name {
    font-size: 26px; font-weight: 400; letter-spacing: 2px;
    color: var(--brand);
  }
  .recipient {
    position: absolute; right: 70px; top: 300px;
    font-size: 14.5px; line-height: 17px; font-style: normal;
    text-align: right;
  }
  .subject {
    position: absolute; left: 66px; top: 420px;
    font-size: 15px; font-weight: 700; letter-spacing: 0.5px;
    color: var(--brand-dark);
  }
  .salutation {
    position: absolute; left: 66px; top: 460px;
    font-size: 16px; font-weight: 700;
  }
  .body-copy {
    position: absolute; left: 66px; top: 500px; width: 726px;
    font-size: 14px; line-height: 16.5px;
  }
  .body-copy p { margin-bottom: 14px; }
  .sender {
    position: absolute; left: 66px; top: 878px;
    font-size: 17px; line-height: 21px;
  }
  .sender-name { font-weight: 700; }
  .sender-email { font-size: 14px; color: var(--brand-dark); }
  .letter-date {
    position: absolute; right: 70px; top: 878px;
    font-size: 15px; line-height: 21px; text-align: right;
  }
  .signature {
    position: absolute; left: 66px; top: 950px;
    width: 140px; height: 66px;
    background: linear-gradient(90deg, var(--signature-tone), transparent);
  }
  .footer-band {
    position: absolute; left: 53px; top: 1106px;
    width: 738px; height: 53px;
    background: linear-gradient(90deg, var(--brand-dark), var(--brand));
    color: var(--footer-text);
    font-size: 13px; text-align: center;
  }
  .footer-company { padding-top: 6px; height: 25px; }
  .footer-rule { margin: 0 14px; height: 1px; background: var(--footer-text); }
  .footer-contacts {
    padding-top: 4px;
    display: flex; justify-content: center; align-items: center; gap: 10px;
  }
  .footer-contacts svg { width: 11px; height: 11px; fill: var(--footer-text); }
  .footer-contacts .item { display: inline-flex; align-items: center; gap: 6px; }
</style>
</head>
<body>
<main class="letterhead">
  <header class="brand">
    <div class="brand-square"></div>
    <div class="brand-name">VELTRANA</div>
  </header>

  <address class="recipient">
    Mr Adrian Holt<br>
    Founder and CEO<br>
    Your Company,<br>
    4120 Cedar Row, Suite 210<br>
    Halden Bay, Canada 51820
  </address>

  <p class="subject">SUBJECT: CIVIL ENGINEER LETTERHEAD</p>
  <p class="salutation">Dear Sir</p>

  <section class="body-copy">
    <p>Lorem ipsum dolor sit amet. Non quam iste ut dolor repellendus aut quasi porro nam molestias ullam ut sint ipsa! Qui accusamus assumenda qui quae tempore sit quia velit aut porro tempora. Est iste explicabo aut alias impedit est sequi quis.</p>
    <p>Cum rerum molestiae id galisum odit et autem voluptas aut blanditiis iste ut aspernatur itaque ut tempora laudantium vel voluptatem repudiandae! Ea delectus omnis est voluptas odit ut assumenda quisquam eos facere sunt qui quis vitae. Qui velit dolorem in distinctio</p>
    <p>dignissimos rem voluptatem totam ut quia nostrum cum quas consequuntur. Quo aliquid earum eum optio ducimus qui fugiat veniam qui blanditiis velit ut quos dolores non officiis enim ut voluptatem veritatis.</p>
    <p>At quia sunt nam quibusdam mollitia aut rerum laudantium et inventore molestiae aut cumque consequatur. 33 minima velit rem quasi galisum ut quae magni sed praesentium possimus 33 commodi quam qui quae aperiam est enim accusantium. Sed Quis laboriosam ut suscipit maxime cum reprehenderit adipisci. Non nihil dolor ut obcaecati commodi aut Quis provident eos doloribus cumque.</p>
    <p>At quia sunt nam quibusdam mollitia aut rerum laudantium et inventore molestiae aut cumque consequatur. 33 minima velit rem quasi galisum ut quae</p>
  </section>

  <div class="sender">
    <div class="sender-name">MARKO VIDAL</div>
    <div class="sender-role">President</div>
    <div class="sender-email">xyz@veltrana.hr</div>
  </div>
  <div class="letter-date">Date: 14 March 2024</div>
  <div class="signature" role="img" aria-label="Handwritten signature of the president"></div>

  <footer class="footer-band">
    <div class="footer-company">Veltrana d.o.o., Lipovac 15, Lipovac (Općina Brdarić), OIB 47396028154</div>
    <div class="footer-rule"></div>
    <div class="footer-contacts">
      <span class="item">
        <svg viewBox="0 0 24 24" aria-hidden="true"><path d="M6.6 10.8a15 15 0 0 0 6.6 6.6l2.2-2.2c.3-.3.7-.4 1-.2 1.1.4 2.3.6 3.6.6.6 0 1 .4 1 1V20c0 .6-.4 1-1 1A17 17 0 0 1 3 4c0-.6.4-1 1-1h3.5c.6 0 1 .4 1 1 0 1.3.2 2.5.6 3.6.1.3 0 .7-.2 1z"/></svg>
        +385 21 480 275
      </span>
      <span class="item">
        <svg viewBox="0 0 24 24" aria-hidden="true"><path d="M2 5h20v14H2z M3 6l9 7 9-7" stroke="#d97f2e" stroke-width="1.5"/></svg>
        info@veltrana.hr
      </span>
      <span class="item">
        <svg viewBox="0 0 24 24" aria-hidden="true"><circle cx="12" cy="12" r="10"/></svg>
        www.veltrana.hr
      </span>
    </div>
  </footer>
</main>
</body>
</html>
```